Postcard Design

Nonprofit agency needs quick turnaround postcard design to help boost attendance at a fundraiser to support a program that helps find homes for children in foster care.

The front should just be the artwork. The back should be the information in an easy to read, attractive layout. The logo and the elevation drawing need to be integrated into the layout.

Industry/Entity Type

It Support

```html
<!DOCTYPE html>
<html lang="en">
<head>
<meta charset="utf-8">
<title>House Party Postcard</title>
<link rel="stylesheet" href="https://fonts.googleapis.com/css2?family=Mulish:wght@300;600;700&display=swap">
<style>
  :root {
    --bg: #3f3f43;
    --paper: #ffffff;
    --green: #1c8a3c;
    --leaf: #6cb33f;
    --ink: #1d1d1d;
    --body: #2a2a2a;
  }
  * { margin: 0; padding: 0; box-sizing: border-box; }
  html, body { width: 1200px; height: 1000px; overflow: hidden; }
  body { background: var(--bg); font-family: "Mulish", Arial, sans-serif; position: relative; }

  .card-front {
    position: absolute; left: 224px; top: 40px; width: 940px; height: 608px;
    background: var(--paper); overflow: hidden;
  }
  .front-artwork {
    position: absolute; left: 110px; top: 0; width: 830px; height: 100%;
    background:
      radial-gradient(ellipse at 85% 10%, #c9d7e6 0 18%, transparent 30%),
      radial-gradient(ellipse at 88% 75%, #c4385a 0 14%, transparent 26%),
      radial-gradient(ellipse at 90% 95%, #f08a2c 0 12%, transparent 22%),
      radial-gradient(ellipse at 55% 30%, #f5c348 0 14%, transparent 26%),
      radial-gradient(ellipse at 30% 35%, #6cc24a 0 16%, transparent 28%),
      radial-gradient(ellipse at 45% 15%, #3a2a26 0 14%, transparent 24%),
      radial-gradient(ellipse at 10% 20%, #3c3c3c 0 14%, transparent 26%),
      linear-gradient(180deg, #eaeaea 0%, #f4f4f4 100%);
  }

  .card-back {
    position: absolute; left: 36px; top: 296px; width: 1032px; height: 668px;
    background: var(--paper);
  }
  .info { position: absolute; left: 22px; top: 30px; width: 425px; }
  .headline { color: var(--green); font-size: 19.5px; font-weight: 600; line-height: 1.2; letter-spacing: -0.1px; }
  .intro, .art-note {
    font-size: 12.6px; font-weight: 300; line-height: 18px; color: var(--body);
    text-align: justify; margin-top: 4px;
  }
  .elevation {
    display: block; width: 425px; height: 196px; margin-top: 15px;
    background: linear-gradient(180deg, #2f9a3a 0%, #2f9a3a 18%, #f3f3f3 20%, #e6e6e6 62%, #b6d436 66%, #a6cc2e 100%);
  }
  .art-note { margin-top: 12px; }
  .galleries, .tickets { font-size: 13.4px; font-weight: 700; line-height: 18.5px; color: var(--ink); }
  .galleries { margin-top: 6px; list-style: none; }
  .tickets { margin-top: 26px; width: 240px; }

  .brand {
    position: absolute; left: 280px; top: 500px; width: 150px;
    display: flex; flex-direction: column; align-items: center; gap: 10px;
  }
  .brand-dot { width: 56px; height: 56px; border-radius: 50%; background: var(--leaf); }
  .brand-name {
    color: var(--leaf); font-size: 17px; font-weight: 700; line-height: 19px; text-align: center;
  }
</style>
</head>
<body>
  <div class="card-front">
    <div class="front-artwork" role="img" aria-label="Artwork of overlapping scalloped shapes in patterned fabrics of green, black, yellow, blue, red and orange"></div>
  </div>

  <div class="card-back">
    <div class="info">
      <h1 class="headline">Nashville’s most exciting Party is almost here!</h1>
      <p class="intro">There are a few tickets left for Harbor Family Service’ House Party, October 30th. This is a preview of the spectacular renovation of the iconic modern Willow Park residence of Dr. and Mrs. Harold Lindqvist, now the home of Marco Velletri and Peter Aldine of Ashby &amp; Rowe. The event will benefit the Bridging Homes program at HFS, which helps prepare foster children for adoption.</p>
      <div class="elevation" role="img" aria-label="Elevation drawing of the white modern residence with green lawn and trees"></div>
      <p class="art-note">The evening will feature an incredible selection of modern art from established and emerging artists personally chosen by the home’s designers/owners and curated by Eleanor M. Hart, of The Hart Art Museum, Louisville. Galleries featured include</p>
      <ul class="galleries">
        <li>The Ellis Crane Gallery, Nashville/Memphis</li>
        <li>The Nora Whitfield Gallery, Nashville</li>
        <li>Mercer Lane Projects, New York</li>
      </ul>
      <p class="tickets">Tickets will sell out and must be purchased in advance.<br>To purchase tickets, please visit www.harborfamilynashville.org or call Clara Denholm West at 615-555-0142.</p>
    </div>
    <div class="brand">
      <span class="brand-dot"></span>
      <span class="brand-name">Harbor Family<br>Service</span>
    </div>
  </div>
</body>
</html>
```